Landing Page Redesign for KT Grounded Form

**Goal:**
To create a website that feels holistic, natural, and reflective of my unique bodywork approach. The new design should speak to individuals seeking proactive solutions to pain through improved posture, alignment, balance, and functional movement patterns. The website should move away from traditional massage associations and instead emphasise my integrative, whole-body focus.

** Business Name:** KT Grounded Form (please do not make the KT into My, the capitals represents the initials of my name.)

**Current Website:**
[www.ktgroundedform.com.au](http://www.ktgroundedform.com.au).

**Overview of Services:**
I specialise in bodywork that integrates functional movement, dynamic cognitive imagery, sensation, and perception to help clients move more efficiently, ease pain, and create long-term changes in posture, balance, and alignment.

**Modalities offered:**
- Dastering and Daster Movement
- Remedial Massage
- Cranio Sacral Therapy

**Target Audience:**
My clients are intelligent individuals who are proactive about their health. They seek a long-term solution to pain, understanding that health is a journey, and they value posture, alignment, and functional movement patterns as part of that solution.

**Tone and Feel:**
The landing page should reflect a holistic and natural approach, with an emphasis on the mind-body connection and the unique benefits of my treatments. It should be professional, warm, and welcoming, evoking balance and movement.

**Design Considerations:**
- **Imagery:**
Avoid traditional massage or spa-like images. Instead, focus on visuals that convey movement, posture, alignment, balance, and flow. Use abstract or anatomy-inspired visuals that reflect the concepts of functional movement and integration. If stock images are needed, suggest options from PixVault or Frameharbor for approval.
- **Colours & Fonts:**
Please refer to the provided brand board for approved colours and fonts.

**Promotional Material:**
I will attach a promotional flyer and my logo for reference so you can see examples of the feel that I like. These will provide guidance on the visual direction for the website.

**Functionality:**
The site should be user-friendly and mobile-responsive, with an easy-to-navigate structure. Key elements should include:
- Clear descriptions of services and approach
- Prominent contact and booking details
- Any suggestions for SEO-optimised for better searchability is appreciated.

**Conclusion:**
The new website should feel aligned with the holistic, natural, and integrative bodywork I offer. It should effectively communicate my approach and attract clients who are looking for a thoughtful, proactive journey towards better posture, alignment, and pain relief.

```html
<!DOCTYPE html>
<html lang="en">
<head>
<meta charset="utf-8">
<title>KT Grounded Form — Healing through Remedial Massage and Dastering</title>
<link rel="stylesheet" href="https://fonts.googleapis.com/css2?family=Montserrat:wght@400;500;600;700&family=Roboto+Slab:wght@600;700&display=swap">
<style>
:root{
  --teal:#7b969c;
  --teal-dark:#6d878d;
  --ink:#2f3336;
  --muted:#555b5e;
  --card:#eef2f2;
  --soft:#f6f7f7;
  --btn-light:#c9d7d5;
  --white:#ffffff;
  --star:#f5a623;
}
*{box-sizing:border-box;margin:0;padding:0}
html,body{width:1200px;height:3863px;overflow:hidden}
body{position:relative;font-family:"Montserrat",sans-serif;color:var(--ink);background:var(--white)}
.abs{position:absolute}

/* header */
.site-header{position:absolute;left:0;top:0;width:1200px;height:81px;background:var(--white);z-index:3}
.nav a{position:absolute;top:33px;font-size:12px;color:var(--teal);text-decoration:none}
.nav a.active{font-weight:600}
.header-btn{position:absolute;left:756px;top:18px;width:171px;height:42px;border:1.5px solid var(--teal);border-radius:3px;color:var(--teal);font-size:11.5px;display:flex;align-items:center;justify-content:center}
.social{position:absolute;width:32px;height:32px;border-radius:50%;border:1px solid #dfe5e6;background:var(--white)}
.brand-badge{position:absolute;left:530px;top:12px;width:140px;height:140px;border-radius:50%;background:var(--white);z-index:4;display:flex;align-items:center;justify-content:center;text-align:center;font-size:15px;font-weight:600;color:var(--teal);line-height:1.25}

/* hero */
.hero{position:absolute;left:0;top:81px;width:1200px;height:546px;background:linear-gradient(180deg,#e9ebe6 0%,#d9d8d0 35%,#a98fa8 62%,#7d6480 100%)}
.hero h1{position:absolute;left:141px;top:146px;font-size:38px;line-height:50px;font-weight:400;color:var(--ink)}
.hero h1 strong{font-weight:700}
.hero-btn{position:absolute;left:142px;top:318px;width:168px;height:41px;background:var(--teal);color:var(--white);font-size:11.5px;border-radius:2px;display:flex;align-items:center;justify-content:center}

/* section titles */
.section-title{position:absolute;left:0;width:1200px;text-align:center;font-size:38px;font-weight:400;color:var(--teal)}
.section-title strong{font-weight:700}
.rule{position:absolute;height:4px;width:30px;background:var(--teal)}

/* services */
.service-card{position:absolute;top:795px;width:296px;height:352px;background:var(--card);border-left:5px solid var(--teal);border-bottom:5px solid var(--teal);border-radius:100px 0 120px 0}
.service-icon{position:absolute;top:-10px;right:-6px;width:82px;height:98px;background:var(--teal);border-radius:36px 0 0 8px}
.service-card h3{position:absolute;left:22px;top:120px;font-size:18px;line-height:25px;font-weight:500;color:var(--teal)}
.service-card p{position:absolute;left:22px;top:185px;width:240px;font-size:11px;line-height:20px;color:var(--ink)}
.service-card .arrow{position:absolute;left:132px;top:298px}

/* about */
.about h2{position:absolute;left:139px;top:1295px;font-size:37px;font-weight:700;color:var(--teal)}
.about .quote{position:absolute;left:142px;top:1365px;font-size:18px}
.about .copy{position:absolute;left:142px;top:1402px;width:460px;font-size:14px;line-height:25.5px}
.about .copy p{margin-bottom:25.5px}
.about .wide{position:absolute;left:142px;top:1850px;width:900px;font-size:14px;line-height:25.5px}
.about .wide p{margin-bottom:25.5px}
.portrait{position:absolute;left:653px;top:1295px;width:417px;height:503px;border-radius:120px 0 150px 0;border-top:5px solid var(--teal);border-right:5px solid var(--teal);background:linear-gradient(160deg,#eef0ee,#d7dad8 60%,#c7c3bd)}

/* reviews */
.reviews{position:absolute;left:0;top:2067px;width:1200px;height:460px;background:var(--soft)}
.review{position:absolute;background:var(--white);border-bottom:5px solid var(--teal);border-left:5px solid var(--teal);border-radius:0 0 0 30px;padding:24px}
.review .name{font-size:15px;font-weight:600}
.review .when{font-size:12px;color:var(--muted);margin-top:4px}
.review .stars{position:absolute;right:22px;top:24px;color:var(--star);font-size:14px;letter-spacing:1px}
.review .text{margin-top:26px;font-size:11px;line-height:18px}
.review-source{position:absolute;left:828px;top:2225px;font-size:24px;font-weight:600;color:var(--teal)}
.carousel-btn{position:absolute;top:2229px;width:28px;height:28px;border-radius:50%}

/* booking */
.booking{position:absolute;left:141px;top:2650px;width:543px;height:410px;background:var(--teal);border-radius:70px 0 0 0}
.booking h2{position:absolute;left:39px;top:46px;font-family:"Roboto Slab",serif;font-size:27px;font-weight:700;color:var(--white);letter-spacing:.3px}
.field{position:absolute;height:42px;background:var(--white);font-size:12px;color:var(--muted);padding-left:14px;display:flex;align-items:center}
.field svg{position:absolute;right:14px;top:17px}
.book-btn{position:absolute;left:39px;top:331px;width:451px;height:42px;background:var(--btn-light);font-size:12.5px;font-weight:600;letter-spacing:.5px;display:flex;align-items:center;justify-content:center}
.booking-photo{position:absolute;left:684px;top:2650px;width:375px;height:410px;border-radius:0 0 90px 0;background:linear-gradient(135deg,#f0ede8 0%,#d9b49c 45%,#c99a80 70%,#eeeae4 100%)}

/* footer */
.site-footer{position:absolute;left:0;top:3152px;width:1200px;height:711px;background:#7f9aa0;color:var(--white)}
.footer-brand{position:absolute;left:530px;top:55px;width:140px;height:140px;border-radius:50%;border:1.5px solid rgba(255,255,255,.6);display:flex;align-items:center;justify-content:center;text-align:center;font-size:15px;font-weight:600;line-height:1.25}
.contact{position:absolute;top:270px}
.contact .ico{position:absolute;left:0;top:0;width:42px;height:42px;border-radius:50%;background:rgba(255,255,255,.18);display:flex;align-items:center;justify-content:center}
.contact h4{position:absolute;left:56px;top:8px;font-size:14px;font-weight:600;letter-spacing:1.5px;white-space:nowrap}
.contact p{position:absolute;left:56px;top:32px;font-size:11px;line-height:19px;white-space:nowrap;color:#eef3f3}
.divider{position:absolute;top:268px;width:1px;height:58px;background:rgba(255,255,255,.35)}
.map{position:absolute;left:141px;top:379px;width:918px;height:214px;background:linear-gradient(90deg,#8fd8ee 0%,#8fd8ee 38%,#e9ecef 46%,#f2f2f2 100%)}
.copyright{position:absolute;left:141px;top:674px;font-size:11.5px}
.footer-social{position:absolute;top:667px;width:26px;height:26px;border-radius:50%;background:var(--white)}
</style>
</head>
<body>

<header class="site-header">
  <nav class="nav">
    <a class="active" href="#" style="left:142px">Home</a>
    <a href="#" style="left:233px">About Us</a>
    <a href="#" style="left:337px">Services</a>
    <a href="#" style="left:438px">Contact</a>
  </nav>
  <div class="header-btn">Book Your Appointment</div>
  <span class="social" style="left:977px;top:23px" aria-label="Social profile"></span>
  <span class="social" style="left:1026px;top:23px" aria-label="Social profile"></span>
</header>
<div class="brand-badge">KT Grounded<br>Form</div>

<section class="hero">
  <div role="img" aria-label="Woman in a red dress with arms raised in a lavender field" style="position:absolute;inset:0"></div>
  <h1><strong>Healing through Remedial</strong><br>Massage and Dastering®<br>Harrow Bay</h1>
  <div class="hero-btn">Book Your Appointment</div>
</section>

<h2 class="section-title" style="top:686px">Services <strong>We Provide</strong></h2>
<span class="rule" style="left:585px;top:740px"></span>

<article class="service-card" style="left:134px">
  <div class="service-icon" role="img" aria-label="Movement pose icon"></div>
  <h3>Dastering and<br>Daster Movement</h3>
  <p>Dastering has the ability to dramatically enhance your posture and structure and potentially resolve discomfort, release tension and alleviate pain.</p>
  <svg class="arrow" width="24" height="12" viewBox="0 0 24 12"><path d="M1 6h21M17 1l5 5-5 5" fill="none" stroke="#7b969c" stroke-width="1.5"/></svg>
</article>
<article class="service-card" style="left:450px">
  <div class="service-icon" role="img" aria-label="Massage therapy icon"></div>
  <h3>Remedial<br>Massage</h3>
  <p>Remedial Massage treatment combines hands-on therapy, targeted techniques and active movement participation to identify and treat your pain whilst...</p>
  <svg class="arrow" width="24" height="12" viewBox="0 0 24 12"><path d="M1 6h21M17 1l5 5-5 5" fill="none" stroke="#7b969c" stroke-width="1.5"/></svg>
</article>
<article class="service-card" style="left:766px">
  <div class="service-icon" role="img" aria-label="Cranio sacral therapy icon"></div>
  <h3>Cranio Sacral<br>Therapy</h3>
  <p>Cranio Sacral Therapy gently releases tension in the body, promoting deep relaxation, pain relief, and a balanced nervous system.</p>
  <svg class="arrow" width="24" height="12" viewBox="0 0 24 12"><path d="M1 6h21M17 1l5 5-5 5" fill="none" stroke="#7b969c" stroke-width="1.5"/></svg>
</article>

<section class="about">
  <h2>Hiya! I’m Kaye</h2>
  <span class="rule" style="left:142px;top:1346px"></span>
  <p class="quote">“I’m not your average massage therapist”</p>
  <div class="copy">
    <p>Break free from chronic pain.&nbsp; Reclaim your mobility.</p>
    <p>You might already know me, but if we haven’t crossed paths yet, I’m your local Remedial Massage Therapist and Certified Daster. I am passionate about providing you with longer lasting pain relief. I want you to reclaim your mobility and move your body with comfort and ease.</p>
    <p>My approach is all about YOU!</p>
    <p>My treatments are gentle with a light touch.&nbsp; You will feel minimal discomfort or pain during a treatment. I am able to help people with acute injuries, constant and chronic pain, long term neurological conditions (like multiple sclerosis, MS). I will work with you to get you out of your chronic pain cycle and to build body awareness. I want you to walk out from a treatment with better breathing, movement and energy.</p>
  </div>
  <div class="wide">
    <p>I trained at overseas training centres as a Certified Daster as this qualification is not available in Australia. I’m a homegrown, Australian, Diploma trained, Remedial Massage Therapist.</p>
    <p><strong>A fun fact about me</strong>: I have a working cocker spaniel who I do as many dog sports with as possible.</p>
  </div>
  <div class="portrait" role="img" aria-label="Portrait of the therapist in a white shirt"></div>
</section>

<section class="reviews">
  <h2 class="section-title" style="top:58px">Client <strong>Reviews</strong></h2>
  <span class="rule" style="left:585px;top:114px"></span>
</section>
<article class="review" style="left:136px;top:2215px;width:354px;height:215px">
  <div class="name">Colin Wardell</div><div class="when">12 months ago</div>
  <div class="stars">★★★★★</div>
  <p class="text">I came for a session not knowing fully what to expect. Working through the session I was not only provided with a great sense of relief but became more aware of my body and what I needed to do to prevent the same level of tension and pain from resuming.</p>
</article>
<article class="review" style="left:508px;top:2240px;width:277px;height:190px;padding:20px 18px">
  <div class="name" style="font-size:14px">Jenna Morrow</div><div class="when" style="font-size:11px">1 year ago</div>
  <div class="stars" style="top:20px;right:18px;font-size:13px">★★★★★</div>
  <p class="text" style="font-size:9.5px;line-height:16px;margin-top:22px">I have had the privilege of undergoing Structural Integration with Kaye at Harrow Bay, and it has been life-changing. Kaye's expertise and genuine care for her clients made the experience exceptional. From the moment I stepped into her inviting space, her warmth put me at ease.</p>
</article>
<div class="review-source">Client</div>
<span class="carousel-btn" style="left:991px;border:1px solid #9aabae"></span>
<span class="carousel-btn" style="left:1030px;background:var(--teal)"></span>
<svg class="abs" style="left:1000px;top:2237px" width="10" height="12" viewBox="0 0 10 12"><path d="M7 1L2 6l5 5" fill="none" stroke="#7b969c" stroke-width="1.5"/></svg>
<svg class="abs" style="left:1040px;top:2237px" width="10" height="12" viewBox="0 0 10 12"><path d="M3 1l5 5-5 5" fill="none" stroke="#fff" stroke-width="1.5"/></svg>
<article class="review" style="left:815px;top:2280px;width:244px;height:150px;padding:18px 18px">
  <div class="name" style="font-size:13px">SunnyLane</div><div class="when" style="font-size:10.5px">1 year ago</div>
  <div class="stars" style="top:18px;right:16px;font-size:12px">★★★★★</div>
  <p class="text" style="font-size:9.5px;line-height:16px;margin-top:20px">An overall positive experience with a reduction in tightness in many areas of my body. I'd highly recommend KT Structural Integration.</p>
</article>

<section class="booking">
  <h2>Book Your Appointment</h2>
  <div class="field" style="left:39px;top:106px;width:451px">Full name</div>
  <div class="field" style="left:39px;top:162px;width:451px">Email</div>
  <div class="field" style="left:39px;top:219px;width:218px">Phone</div>
  <div class="field" style="left:272px;top:219px;width:218px">Service type<svg width="12" height="8" viewBox="0 0 12 8"><path d="M1 1l5 5 5-5" fill="none" stroke="#333" stroke-width="1.6"/></svg></div>
  <div class="field" style="left:39px;top:276px;width:218px">Date<svg width="12" height="8" viewBox="0 0 12 8"><path d="M1 1l5 5 5-5" fill="none" stroke="#333" stroke-width="1.6"/></svg></div>
  <div class="field" style="left:272px;top:276px;width:218px">Time<svg width="12" height="8" viewBox="0 0 12 8"><path d="M1 1l5 5 5-5" fill="none" stroke="#333" stroke-width="1.6"/></svg></div>
  <div class="book-btn" style="top:331px">BOOK NOW</div>
</section>
<div class="booking-photo" role="img" aria-label="Hands-on back treatment photo"></div>

<footer class="site-footer">
  <div class="footer-brand">KT Grounded<br>Form</div>

  <div class="contact" style="left:141px">
    <span class="ico"><svg width="16" height="12" viewBox="0 0 16 12"><rect x="0.5" y="0.5" width="15" height="11" rx="1" fill="#fff"/><path d="M1 1l7 6 7-6" fill="none" stroke="#7f9aa0" stroke-width="1.4"/></svg></span>
    <h4>EMAIL ADDRESS</h4>
    <p>ktgroundedform@mailbox.example</p>
  </div>
  <span class="divider" style="left:428px"></span>
  <div class="contact" style="left:482px">
    <span class="ico"><svg width="14" height="18" viewBox="0 0 14 18"><path d="M7 1a6 6 0 0 0-6 6c0 4 6 10 6 10s6-6 6-10a6 6 0 0 0-6-6z" fill="none" stroke="#fff" stroke-width="1.6"/><circle cx="7" cy="7" r="2" fill="#fff"/></svg></span>
    <h4>LOCATION</h4>
    <p>Lakeview Rooms, Suite 2b, Level 1, 318<br>Shore Road Harrow Bay, NSW 2290</p>
  </div>
  <span class="divider" style="left:840px"></span>
  <div class="contact" style="left:892px">
    <span class="ico"><svg width="16" height="16" viewBox="0 0 16 16"><path d="M3 1l3 3-2 2c1 2 3 4 6 6l2-2 3 3-2 3C7 15 1 9 1 3z" fill="#fff"/></svg></span>
    <h4>CONTACT NO</h4>
    <p>0400 123 987</p>
  </div>

  <div class="map" role="img" aria-label="Street map showing the clinic location by the lake"></div>

  <p class="copyright">© 2024 KT Grounded Form. All Rights Reserved.</p>
  <span class="footer-social" style="left:995px" aria-label="Social profile"></span>
  <span class="footer-social" style="left:1033px" aria-label="Social profile"></span>
</footer>

</body>
</html>
```